Plakat-Design für Immobilienmakler
Zielgruppe
Wir sind Immobilienmakler
Aufgabenstellung
Benötigen die Datei für eine Schaufenstervollbeklebung.
Maße: Bx 1,99m, H 1,70m
Ist direkt in der Stadt an der Straße.
Soll schick, edel aussehen und unsere Leistungen aufzeigen.
z.B.
Lehnen Sie sich zurück wir kümmern uns um Ihre Immobilie!
oder
Wir haben den passenden Käufer für Ihre Immobilie!
- kaufen
- verkaufen
- makeln
- Home Staging
- Hausmeisterservice
Ihr Immobilienmakler in Gaildorf, Schwäbisch Hall, Backnang

```html
<!DOCTYPE html>
<html lang="de">
<head>
<meta charset="utf-8">
<title>Schaufensterplakat – Talblick Immobilien</title>
<link rel="stylesheet" href="https://fonts.googleapis.com/css2?family=Montserrat:wght@400;700&family=Caveat:wght@600&display=swap">
<style>
  :root {
    --gold: #c9a04f;
    --blue: #1f5d9a;
    --band: #1b5896;
    --night: #050506;
    --room: #1a1a1c;
    --floor-light: #b9b9b9;
    --floor-dark: #6e6e6e;
    --page: #ffffff;
  }
  * { margin: 0; padding: 0; box-sizing: border-box; }
  html, body { width: 1200px; height: 2268px; overflow: hidden; background: var(--page); }
  .poster {
    position: absolute; left: 40px; top: 656px; width: 1120px; height: 956px;
    overflow: hidden;
    background: radial-gradient(ellipse 900px 420px at 75% 0%, #2e2e31 0%, var(--room) 45%, var(--night) 100%);
    box-shadow: 0 12px 30px rgba(0,0,0,.35);
    font-family: "Montserrat", sans-serif;
  }
  .room-curve { position: absolute; left: 0; top: 0; width: 1120px; height: 668px; }
  .floor {
    position: absolute; left: 0; top: 668px; width: 1120px; height: 234px;
    background: linear-gradient(180deg, #8a8a8a 0%, var(--floor-light) 30%, #9c9c9c 70%, var(--floor-dark) 100%);
  }
  .floor::before {
    content: ""; position: absolute; left: 0; top: 0; width: 100%; height: 10px;
    background: linear-gradient(180deg, #d4d4d4, #7a7a7a);
  }
  .portrait {
    position: absolute; left: 655px; top: 0; width: 465px; height: 902px;
    background:
      linear-gradient(90deg, rgba(8,8,9,1) 0%, rgba(8,8,9,0) 35%),
      radial-gradient(ellipse 90px 120px at 62% 18%, #8f8f8f 0%, rgba(0,0,0,0) 100%),
      radial-gradient(ellipse 200px 330px at 50% 45%, #bcbcbc 0%, #6a6a6a 55%, rgba(20,20,20,0) 100%),
      linear-gradient(180deg, #5c5c5c 0%, #2a2a2a 55%, rgba(60,60,60,.5) 100%);
  }
  .headline {
    position: absolute; right: 405px; top: 66px; width: 700px;
    text-align: right; color: var(--gold);
    font-weight: 400; font-size: 52px; line-height: 64px; letter-spacing: .5px;
  }
  .services {
    position: absolute; right: 405px; top: 268px;
    color: var(--blue); font-size: 16px; white-space: nowrap;
  }
  .region-claim {
    position: absolute; left: 70px; top: 490px; width: 540px;
    color: var(--gold); font-family: "Caveat", cursive; font-weight: 600;
    font-size: 40px; line-height: 56px; text-align: center; white-space: nowrap;
    transform: rotate(-8deg); transform-origin: center;
  }
  .brand {
    position: absolute; left: 500px; top: 642px;
    display: flex; align-items: center; gap: 10px;
  }
  .brand-mark { width: 16px; height: 16px; background: var(--gold); }
  .brand-name { color: var(--blue); font-weight: 700; font-size: 24px; white-space: nowrap; }
  .contact-icon { position: absolute; top: 835px; width: 54px; height: 54px; }
  .contact-band {
    position: absolute; left: 0; top: 902px; width: 1120px; height: 54px;
    background: var(--band);
    display: flex; justify-content: center; align-items: center; gap: 20px;
    color: var(--gold); font-weight: 700; font-size: 17px; white-space: nowrap;
  }
</style>
</head>
<body>
<main class="poster">
  <svg class="room-curve" viewBox="0 0 1120 668" aria-hidden="true">
    <path d="M0 668 C 120 420, 420 300, 1120 300 L1120 0 L0 0 Z" fill="#ffffff" opacity=".04"/>
  </svg>

  <div class="floor" role="img" aria-label="Heller Holzdielenboden in Grautönen"></div>
  <div class="portrait" role="img" aria-label="Schwarzweißfoto einer Frau im schwarzen Kleid, entspannt in einem Ohrensessel sitzend"></div>

  <h1 class="headline">Lehnen Sie sich zurück<br>wir kümmern uns um<br>Ihre Immobilie!</h1>
  <p class="services">kaufen | verkaufen | makeln | Home Staging | Hausmeisterservice</p>

  <p class="region-claim">Ihr Immobilienmakler in<br>Gaildorf, Schwäbisch Hall, Backnang</p>

  <div class="brand">
    <span class="brand-mark"></span>
    <span class="brand-name">Talblick Immobilien</span>
  </div>

  <svg class="contact-icon" style="left:173px" viewBox="0 0 48 48" aria-hidden="true">
    <path d="M12 6 L18 6 L21 15 L16 19 C18 26 22 30 29 32 L33 27 L42 30 L42 36 C42 40 39 42 35 42 C20 41 7 28 6 13 C6 9 8 6 12 6 Z" fill="none" stroke="var(--blue)" stroke-width="2.5" stroke-linejoin="round"/>
  </svg>
  <svg class="contact-icon" style="left:521px" viewBox="0 0 48 48" aria-hidden="true">
    <path d="M44 4 L6 22 L20 28 L26 42 Z M20 28 L44 4" fill="none" stroke="var(--blue)" stroke-width="2.5" stroke-linejoin="round"/>
    <path d="M8 40 L15 33 M4 34 L10 28" stroke="var(--blue)" stroke-width="2.5" stroke-linecap="round"/>
  </svg>
  <svg class="contact-icon" style="left:886px" viewBox="0 0 48 48" aria-hidden="true">
    <rect x="5" y="6" width="38" height="28" rx="2" fill="none" stroke="var(--blue)" stroke-width="2.5"/>
    <path d="M24 34 L24 41 M16 42 L32 42" stroke="var(--blue)" stroke-width="2.5" stroke-linecap="round"/>
  </svg>

  <footer class="contact-band">
    <span>+49 (0) 15 2 / 00 48 27 19</span><span>|</span>
    <span>info@talblick-immobilien.de</span><span>|</span>
    <span>www.talblick-immobilien.de</span>
  </footer>
</main>
</body>
</html>
```